Business Card Design Project

I need a business card design for our new logo, please check the logo at the following link:
https://www.filecrate.net/s/q7rtx2pw9kd41m/FernLoop.png
The address on the business card:
Av. Gervásio Tavares 418 sala 207
Jardim Aurora, Porto Serrano, PS
CEP: 22714-380
Brasil
Phone: +55 21 86347215
e-mail: osvaldo@fernloop.com.br
Updates
Thank you all for sending your designs, we will not provide feedback because there are too many designs, on December 3 we will pick the best design according to our point of view. Please keep posting.
Osvaldo
Industry/Entity Type
Business
Look and feel
Each slider illustrates characteristics of the customer's brand and the style your logo design should communicate.

```html
<!DOCTYPE html>
<html lang="pt-BR">
<head>
<meta charset="utf-8">
<title>FernLoop – Business Card</title>
<link rel="stylesheet" href="https://fonts.googleapis.com/css2?family=Open+Sans:wght@400;600;800&display=swap">
<style>
  :root {
    --paper: #ffffff;
    --ink: #1c1c1c;
    --muted: #6a6a6a;
    --accent: #f5c000;
    --backdrop: #e9e6e1;
    --rule: #d8d8d8;
  }
  * { box-sizing: border-box; margin: 0; padding: 0; }
  html, body { width: 1200px; height: 900px; overflow: hidden; }
  body {
    background: var(--backdrop);
    font-family: "Open Sans", sans-serif;
    color: var(--ink);
    position: relative;
  }
  .card {
    position: absolute;
    left: 300px;
    width: 600px;
    height: 343px;
    background: var(--paper);
    box-shadow: 0 6px 18px rgba(0,0,0,.12);
    overflow: hidden;
  }
  .card--front { top: 78px; }
  .card--back { top: 479px; }
  .card__bands { position: absolute; inset: 0; width: 100%; height: 100%; }

  .brand {
    position: absolute;
    display: flex;
    align-items: center;
    gap: 10px;
  }
  .brand__dot {
    width: 22px; height: 22px; border-radius: 50%;
    background: var(--accent);
  }
  .brand__name {
    font-weight: 800;
    font-size: 38px;
    letter-spacing: -0.5px;
    color: var(--ink);
  }
  .card--front .brand { left: 50%; top: 110px; transform: translateX(-50%); }
  .card--back .brand { left: 60px; top: 150px; }

  .web {
    position: absolute;
    right: 120px; top: 226px;
    font-weight: 600;
    font-size: 14px;
    letter-spacing: .3px;
  }

  .contact {
    position: absolute;
    left: 345px; top: 52px;
    width: 235px;
  }
  .contact__name {
    color: var(--accent);
    font-weight: 600;
    font-size: 19px;
    padding-bottom: 3px;
    border-bottom: 1px solid var(--rule);
  }
  .contact__role { font-size: 10px; color: var(--muted); margin-top: 4px; }
  .contact__list { list-style: none; margin-top: 26px; font-size: 11px; line-height: 1.55; color: #333; }
  .contact__list li { display: flex; gap: 7px; align-items: flex-start; }
  .contact__icon { flex: 0 0 11px; margin-top: 3px; fill: var(--accent); }
</style>
</head>
<body>

<section class="card card--front" aria-label="Card front">
  <svg class="card__bands" viewBox="0 0 600 343" aria-hidden="true">
    <polygon points="0,268 470,268 488,252 500,252 480,282 0,282" fill="var(--accent)"/>
    <polygon points="508,252 600,252 600,282 488,282" fill="var(--ink)"/>
  </svg>
  <div class="brand">
    <span class="brand__dot"></span>
    <span class="brand__name">FernLoop</span>
  </div>
  <p class="web">www.fernloop.com.br</p>
</section>

<section class="card card--back" aria-label="Card back">
  <svg class="card__bands" viewBox="0 0 600 343" aria-hidden="true">
    <line x1="300" y1="70" x2="326" y2="270" stroke="var(--rule)" stroke-width="1.2"/>
    <polygon points="0,300 505,300 530,275 600,275 600,288 548,288 520,318 0,318" fill="var(--ink)"/>
    <polygon points="540,275 600,275 600,288 528,288" fill="var(--accent)"/>
  </svg>
  <div class="brand">
    <span class="brand__dot"></span>
    <span class="brand__name">FernLoop</span>
  </div>
  <div class="contact">
    <p class="contact__name">Osvaldo Osvaldo</p>
    <p class="contact__role">Owner</p>
    <ul class="contact__list">
      <li>
        <svg class="contact__icon" viewBox="0 0 12 12" width="11" height="11"><path d="M3 1l2 2.5-1.2 1.2a7 7 0 0 0 3.5 3.5L8.5 7 11 9l-1.5 2A9 9 0 0 1 1 2.5z"/></svg>
        +55 21 86347215
      </li>
      <li>
        <svg class="contact__icon" viewBox="0 0 12 12" width="11" height="11"><path d="M1 2.5h10v7H1z M1 2.5l5 4 5-4" stroke="#fff" stroke-width=".8"/></svg>
        osvaldo@fernloop.com.br
      </li>
      <li>
        <svg class="contact__icon" viewBox="0 0 12 12" width="11" height="11"><path d="M6 1l5 4.5H9.5V11h-7V5.5H1z"/></svg>
        <span>Av. Gervásio Tavares 418 sala 207<br>Jardim Aurora, Porto Serrano,<br>PS CEP: 22714-380 Brasil</span>
      </li>
    </ul>
  </div>
</section>

</body>
</html>
```